Standardization and redesign of graphics for a non-fiction book

For a book project, 11 graphics need to be visually unified so that all the graphics in the book are in the same style. The graphics must be created from scratch. Just new colors aren't enough. Some of the existing graphics are by other authors who own the copyright. Accordingly, the new graphics must be truly new. This is especially true for the "2 S-curves" graphic.

Target Market(s)

Manager Furniture Industry

Industry/Entity Type

Möbel

Colors
0054AA
0677BA
7BADD7
CADEEF
E8F1F8

```html
<!DOCTYPE html>
<html lang="de">
<head>
<meta charset="utf-8">
<title>Entwicklung des deutschen Möbelhandels 2014 – 2024</title>
<link rel="stylesheet" href="https://fonts.googleapis.com/css2?family=Poppins:ital,wght@0,400;0,700;1,400&display=swap">
<style>
  :root {
    --brand-blue: #0a4bb3;
    --axis-text: #6e6e6e;
    --grid-line: #a8a8a8;
    --store-area: #e6e6e6;
    --online-start: #17a8d4;
    --online-end: #2bfff5;
    --share-start: #3f9de2;
    --share-end: #0046ae;
    --page-bg: #ffffff;
  }
  html, body {
    margin: 0;
    padding: 0;
    width: 1200px;
    height: 1200px;
    overflow: hidden;
    background: var(--page-bg);
  }
  .chart {
    display: block;
    width: 1200px;
    height: 1200px;
    font-family: "Poppins", sans-serif;
  }
  .chart-title { fill: var(--brand-blue); font-weight: 700; font-size: 32px; }
  .chart-subtitle { fill: var(--brand-blue); font-style: italic; font-size: 26px; }
  .axis-label { fill: var(--axis-text); font-size: 17px; }
  .legend-label { fill: var(--axis-text); font-size: 17px; }
  .grid-line { stroke: var(--grid-line); stroke-width: 1; }
  .store-area { fill: var(--store-area); }
  .share-line { fill: none; stroke: url(#shareGradient); stroke-width: 6; stroke-linejoin: round; }
</style>
</head>
<body>
<svg class="chart" viewBox="0 0 1500 1500" xmlns="http://www.w3.org/2000/svg" role="img" aria-label="Diagramm: Entwicklung des deutschen Möbelhandels 2014 bis 2024, stationäre und online Umsätze in Mrd Euro sowie Online-Anteil in Prozent">
  <defs>
    <linearGradient id="onlineGradient" x1="320" y1="0" x2="1181" y2="0" gradientUnits="userSpaceOnUse">
      <stop offset="0" stop-color="var(--online-start)"/>
      <stop offset="1" stop-color="var(--online-end)"/>
    </linearGradient>
    <linearGradient id="shareGradient" x1="312" y1="0" x2="1190" y2="0" gradientUnits="userSpaceOnUse">
      <stop offset="0" stop-color="var(--share-start)"/>
      <stop offset="1" stop-color="var(--share-end)"/>
    </linearGradient>
    <linearGradient id="legendOnline" x1="0" y1="0" x2="1" y2="0">
      <stop offset="0" stop-color="var(--online-start)"/>
      <stop offset="1" stop-color="var(--online-end)"/>
    </linearGradient>
    <linearGradient id="legendShare" x1="0" y1="0" x2="1" y2="0">
      <stop offset="0" stop-color="var(--share-end)"/>
      <stop offset="1" stop-color="var(--share-start)"/>
    </linearGradient>
  </defs>

  <g class="chart-heading" text-anchor="middle">
    <text class="chart-title" x="745" y="514">Entwicklung des deutschen Möbelhandels 2014 – 2024</text>
    <text class="chart-subtitle" x="746" y="548">in Mrd Euro</text>
  </g>

  <g class="grid">
    <line class="grid-line" x1="237" x2="1255" y1="590" y2="590"/>
    <line class="grid-line" x1="237" x2="1255" y1="631" y2="631"/>
    <line class="grid-line" x1="237" x2="1255" y1="672" y2="672"/>
    <line class="grid-line" x1="237" x2="1255" y1="715" y2="715"/>
    <line class="grid-line" x1="237" x2="1255" y1="756" y2="756"/>
    <line class="grid-line" x1="237" x2="1255" y1="797" y2="797"/>
    <line class="grid-line" x1="237" x2="1255" y1="838" y2="838"/>
    <line class="grid-line" x1="237" x2="1255" y1="882" y2="882"/>
    <line class="grid-line" x1="237" x2="1255" y1="920" y2="920"/>
  </g>

  <g class="axis-left" text-anchor="end">
    <text class="axis-label" x="226" y="586">40.000</text>
    <text class="axis-label" x="226" y="631">35.000</text>
    <text class="axis-label" x="226" y="672">30.000</text>
    <text class="axis-label" x="226" y="716">25.000</text>
    <text class="axis-label" x="226" y="757">20.000</text>
    <text class="axis-label" x="226" y="798">15.000</text>
    <text class="axis-label" x="226" y="839">10.000</text>
    <text class="axis-label" x="226" y="882">5.000</text>
    <text class="axis-label" x="226" y="921">0.000</text>
  </g>

  <g class="axis-right" text-anchor="start">
    <text class="axis-label" x="1274" y="586">20.0%</text>
    <text class="axis-label" x="1274" y="627">18.0%</text>
    <text class="axis-label" x="1274" y="662">16.0%</text>
    <text class="axis-label" x="1274" y="698">14.0%</text>
    <text class="axis-label" x="1274" y="730">12.0%</text>
    <text class="axis-label" x="1274" y="763">10.0%</text>
    <text class="axis-label" x="1274" y="795">8.0%</text>
    <text class="axis-label" x="1274" y="827">6.0%</text>
    <text class="axis-label" x="1274" y="857">4.0%</text>
    <text class="axis-label" x="1274" y="888">2.0%</text>
    <text class="axis-label" x="1274" y="920">0.0%</text>
  </g>

  <polygon class="store-area" points="320,920 320,679 404,679 495,665 665,671 750,665 922,668 1007,652 1097,660 1181,679 1181,920"/>

  <polygon class="online-area" fill="url(#onlineGradient)" points="320,667 404,667 495,645 665,642 750,632 922,624 1007,611 1097,625 1181,642 1181,679 1097,660 1007,652 922,668 750,665 665,671 495,665 404,679 320,679"/>

  <polyline class="share-line" points="312,839 404,822 495,806 580,777 665,763 750,748 922,694 1097,740 1190,717"/>

  <g class="axis-bottom" text-anchor="middle">
    <text class="axis-label" x="294" y="968">2014</text>
    <text class="axis-label" x="339" y="968">|</text>
    <text class="axis-label" x="383" y="968">2015</text>
    <text class="axis-label" x="428" y="968">|</text>
    <text class="axis-label" x="472" y="968">2016</text>
    <text class="axis-label" x="516" y="968">|</text>
    <text class="axis-label" x="560" y="968">2017</text>
    <text class="axis-label" x="604" y="968">|</text>
    <text class="axis-label" x="648" y="968">2018</text>
    <text class="axis-label" x="692" y="968">|</text>
    <text class="axis-label" x="737" y="968">2019</text>
    <text class="axis-label" x="781" y="968">|</text>
    <text class="axis-label" x="828" y="968">2020</text>
    <text class="axis-label" x="875" y="968">|</text>
    <text class="axis-label" x="919" y="968">2021</text>
    <text class="axis-label" x="963" y="968">|</text>
    <text class="axis-label" x="1009" y="968">2022</text>
    <text class="axis-label" x="1055" y="968">|</text>
    <text class="axis-label" x="1102" y="968">2023</text>
    <text class="axis-label" x="1148" y="968">|</text>
    <text class="axis-label" x="1195" y="968">2024</text>
  </g>

  <g class="legend">
    <rect x="400" y="1019" width="23" height="18" fill="var(--store-area)"/>
    <text class="legend-label" x="437" y="1034">stationäre Umsätze</text>
    <rect x="650" y="1019" width="23" height="18" fill="url(#legendOnline)"/>
    <text class="legend-label" x="684" y="1034">online Umsätze</text>
    <rect x="853" y="1019" width="23" height="18" fill="url(#legendShare)"/>
    <text class="legend-label" x="887" y="1034">online Umsätze</text>
  </g>
</svg>
</body>
</html>
```